Corporate Business Card

Very professional, Modern, Not to busy, include phone address email, website
(253) 555-0174, 61807 19th Street N, Kent, WA 98517, marcus@kestrelbayholding.com, brelvanindustries.com

Target Market(s)

Manufacturing

Industry/Entity Type

Aero, machining, manufacturing, Off road racing

Contact Information for Business Card

Phone, address email, website

```html
<!DOCTYPE html>
<html lang="en">
<head>
<meta charset="utf-8">
<title>Brelvan Industries – Business Card</title>
<link rel="stylesheet" href="https://fonts.googleapis.com/css2?family=Open+Sans:wght@400;600;700&display=swap">
<style>
  :root {
    --navy: #1b3577;
    --navy-deep: #16306e;
    --red: #d4202a;
    --ink: #1f2230;
    --paper: #ffffff;
    --backdrop: #e9e9ea;
  }
  * { margin: 0; padding: 0; box-sizing: border-box; }
  html, body {
    width: 1084px; height: 1200px; overflow: hidden;
    background: var(--backdrop);
    font-family: "Open Sans", Arial, sans-serif;
  }
  .card {
    position: absolute; left: 112px;
    width: 860px; height: 491px;
    box-shadow: 0 6px 14px rgba(0,0,0,.22);
    overflow: hidden;
  }
  .card-back { top: 70px; background: var(--navy-deep); }
  .card-front { top: 630px; background: var(--paper); }

  .back-pattern {
    position: absolute; inset: 0;
    background: linear-gradient(135deg, #1a3a7a 0%, #16306e 55%, #142b64 100%);
  }
  .back-brand {
    position: absolute; left: 520px; top: 360px;
    display: flex; align-items: center; gap: 10px;
    color: #ffffff; font-weight: 700; font-size: 25px; letter-spacing: .5px;
  }
  .back-brand .mark { width: 14px; height: 14px; background: var(--red); }

  .front-brand {
    position: absolute; left: 84px; top: 205px;
    display: flex; align-items: center; gap: 12px;
    color: var(--navy); font-weight: 700; font-size: 30px; letter-spacing: .5px;
    line-height: 1.1;
  }
  .front-brand .mark { width: 18px; height: 18px; background: var(--red); flex: none; }

  .contact { position: absolute; left: 457px; top: 100px; color: var(--ink); }
  .contact .name {
    color: var(--navy); font-weight: 600; font-size: 33px; line-height: 1.1; letter-spacing: .2px;
  }
  .contact .role { font-size: 24px; line-height: 1.25; }
  .contact .address { margin-top: 44px; font-size: 22px; line-height: 1.35; }
  .contact .lines { margin-top: 28px; font-size: 22px; line-height: 1.45; }
  .contact .line { display: flex; align-items: center; gap: 8px; }
  .contact .icon { width: 16px; height: 16px; flex: none; }

  .swoosh { position: absolute; left: 0; bottom: 0; width: 860px; height: 100px; }
  .website {
    position: absolute; right: 100px; bottom: 10px;
    color: #ffffff; font-weight: 600; font-size: 21px;
  }
</style>
</head>
<body>

<section class="card card-back">
  <div class="back-pattern" role="img" aria-label="Faint repeated brand name pattern in tonal blue"></div>
  <div class="back-brand"><span class="mark"></span>Brelvan Industries</div>
</section>

<section class="card card-front">
  <div class="front-brand"><span class="mark"></span>Brelvan<br>Industries</div>

  <div class="contact">
    <p class="name">DANIEL HARTWELL</p>
    <p class="role">Account Manager</p>
    <p class="address">61807 19th Street N<br>Kent, WA 98517</p>
    <div class="lines">
      <p class="line">
        <svg class="icon" viewBox="0 0 16 16" aria-hidden="true"><path fill="#d4202a" d="M3.5 1.5l2.5 3-1.5 1.8c.9 2 2.3 3.4 4.2 4.2L10.5 9l3 2.5-1.2 2.5C6.5 14 2 9.5 1.5 3.2z"/></svg>
        (253) 555-0174
      </p>
      <p class="line">
        <svg class="icon" viewBox="0 0 16 16" aria-hidden="true"><rect x="1" y="3.5" width="14" height="9" fill="#d4202a"/><path d="M1.5 4l6.5 5 6.5-5" fill="none" stroke="#fff" stroke-width="1.2"/></svg>
        marcus@kestrelbayholding.com
      </p>
    </div>
  </div>

  <svg class="swoosh" viewBox="0 0 860 100" preserveAspectRatio="none" aria-hidden="true">
    <path fill="#d4202a" d="M0 100 C180 62 420 44 645 42 L560 48 C380 55 180 78 70 100 Z"/>
    <path fill="#1b3577" d="M175 100 C380 62 620 52 860 47 L860 100 Z"/>
  </svg>
  <p class="website">www.brelvanindustries.com</p>
</section>

</body>
</html>
```